Cardiology Practice needs a Heart Scan Order Form

Busy cardiology practice needs an order form for a heart scan test. Sample is attached. One side should have all information noted and the other side should have our physician names (Vikram Joshi, MD, K.L. Morvandi, MD, Anjali Desai, MD, Parvin Joshi, MD, and Gerald Montefino, MD. It should have the map that is uploaded and our demographic information (Crestline Cardio PLLC, 218 Juniper Ave. Ste. B, Webster, TX 77412 along with phone 713-642-1187 and fax 713-642-1188) as well as our web address (crestlinecardio.example). Our primary colors are red, black and white. Needs to fit paper size 8 1/2 by 11.

Target Market(s)

Healthcare

Industry/Entity Type

Health Care

Font styles to use
Serif

Colors
ec1f27

Requirements
Must have
• Logo, information listed on sample form, demographics and physician names as well as website.
Nice to have
• Open to suggestions
Should not have
• Physician Pictures

```html
<!DOCTYPE html>
<html lang="en">
<head>
<meta charset="utf-8">
<title>Calcium Score Heart Scan – Order Form</title>
<link rel="stylesheet" href="https://fonts.googleapis.com/css2?family=Montserrat:wght@400;700&family=Roboto+Condensed:wght@300;400;700&display=swap">
<style>
:root{
  --ink:#231f20;
  --red:#e3242b;
  --peach:#f7c9b9;
  --rule:#3a3a3a;
  --paper:#ffffff;
}
*{box-sizing:border-box;margin:0;padding:0}
html,body{width:927px;height:1200px;overflow:hidden;background:var(--paper)}
.form{position:relative;width:927px;height:1200px;color:var(--ink);font-family:"Roboto Condensed",sans-serif;font-weight:300}
.abs{position:absolute;white-space:nowrap}
.brand{left:62px;top:44px;font-family:"Roboto Condensed",sans-serif;font-weight:700;font-size:25px;color:var(--red);letter-spacing:.5px}
.brand-mark{left:62px;top:78px;width:10px;height:10px;background:var(--red)}
.physicians{left:248px;top:52px;width:608px;display:flex;justify-content:space-between;font-family:Montserrat,sans-serif;font-size:11.2px;color:var(--ink)}
.physicians-rule{left:248px;top:70px;width:608px;height:2px;background:var(--red)}
.title{left:64px;top:166px;font-family:Montserrat,sans-serif;font-size:33px;font-weight:400;letter-spacing:-.3px}
.title b{font-weight:700}
.band{position:absolute;background:var(--peach);font-weight:700;font-size:13px;display:flex;align-items:center;justify-content:center;color:var(--ink)}
.field{position:absolute;font-size:12.5px}
.line{position:absolute;height:1px;background:var(--rule)}
.sched-row{position:absolute;left:657px;width:199px;border-bottom:1px solid var(--rule);font-size:14px;padding-left:6px;height:24px;line-height:24px}
.box{position:absolute;width:12px;height:12px;border:1px solid var(--ink)}
.sexbox{position:absolute;width:34px;height:22px;border:1px solid var(--ink);font-size:11px;text-align:center;line-height:20px}
.alert{left:64px;top:624px;width:792px;height:26px;background:var(--red);color:#fff;font-weight:700;font-size:11px;display:flex;align-items:center;justify-content:center}
.steps{position:absolute;left:65px;top:673px;width:790px;list-style:none;font-size:14.5px;line-height:15px}
.steps li{position:absolute;left:0;padding-left:21px;width:790px}
.steps li::before{content:"";position:absolute;left:0;top:4px;width:8px;height:8px;border:1px solid var(--ink)}
.steps b{font-weight:700}
.ack{left:64px;top:944px;font-size:14.5px;line-height:16px;white-space:normal;width:790px}
.sig-label{position:absolute;width:213px;text-align:center;font-size:12.5px}
.footer{left:64px;top:1124px;color:var(--red);font-size:12.5px;line-height:16px}
.footer b{font-weight:700}
</style>
</head>
<body>
<main class="form">
  <span class="abs brand-mark"></span>
  <div class="abs brand" style="left:78px;top:66px">Crestline Cardio</div>

  <div class="abs physicians">
    <span>Vikram Joshi, M.D.</span><span>K.L. Morvandi, M.D.</span><span>Anjali Desai, M.D.</span><span>Parvin Joshi, M.D.</span><span>Gerald Montefino, M.D.</span>
  </div>
  <div class="abs physicians-rule"></div>

  <div class="band" style="left:657px;top:125px;width:199px;height:24px;font-size:14px">TEST SCHEDULE</div>
  <div class="sched-row" style="top:150px">Test date:</div>
  <div class="sched-row" style="top:174px">Test time:</div>

  <h1 class="abs title"><b>CALCIUM SCORE</b> HEART SCAN</h1>

  <!-- patient / contact -->
  <div class="band" style="left:64px;top:226px;width:385px;height:21px">PATIENT INFORMATION</div>
  <div class="band" style="left:471px;top:226px;width:385px;height:21px">CONTACT INFORMATION</div>
  <span class="field" style="left:64px;top:257px">Last name</span>
  <span class="field" style="left:231px;top:257px">First name</span>
  <span class="field" style="left:386px;top:257px">MI</span>
  <span class="field" style="left:471px;top:257px">Address</span>
  <div class="line" style="left:64px;top:290px;width:385px"></div>
  <div class="line" style="left:471px;top:290px;width:385px"></div>
  <span class="field" style="left:64px;top:305px">Date of birth</span>
  <span class="field" style="left:279px;top:305px">Account no.</span>
  <span class="field" style="left:471px;top:305px">Home phone no.</span>
  <span class="field" style="left:686px;top:305px">Mobile phone no.</span>
  <div class="line" style="left:64px;top:339px;width:170px"></div>
  <div class="line" style="left:279px;top:339px;width:170px"></div>
  <div class="line" style="left:471px;top:339px;width:170px"></div>
  <div class="line" style="left:686px;top:339px;width:170px"></div>

  <!-- medical -->
  <div class="band" style="left:64px;top:372px;width:792px;height:21px">MEDICAL INFORMATION</div>
  <span class="field" style="left:64px;top:407px">Sex:</span>
  <span class="sexbox" style="left:93px;top:404px">F</span>
  <span class="sexbox" style="left:137px;top:404px">M</span>
  <span class="field" style="left:234px;top:409px">Height:</span><div class="line" style="left:270px;top:425px;width:121px"></div>
  <span class="field" style="left:442px;top:409px">Weight:</span><div class="line" style="left:477px;top:425px;width:121px"></div>
  <span class="field" style="left:646px;top:409px">Race:</span><div class="line" style="left:674px;top:425px;width:182px"></div>
  <span class="field" style="left:64px;top:447px">Diagnosis:</span><div class="line" style="left:113px;top:463px;width:743px"></div>

  <span class="box" style="left:64px;top:489px"></span><span class="field" style="left:87px;top:488px">PCI&nbsp; (no. of stents: <span style="display:inline-block;width:70px;border-bottom:1px solid var(--rule)"></span>)</span>
  <span class="box" style="left:305px;top:489px"></span><span class="field" style="left:328px;top:488px">CABG (no. of vessels: <span style="display:inline-block;width:56px;border-bottom:1px solid var(--rule)"></span>)</span>
  <span class="box" style="left:545px;top:489px"></span><span class="field" style="left:568px;top:488px">MI (last event: <span style="display:inline-block;width:92px;border-bottom:1px solid var(--rule)"></span> )</span>
  <span class="box" style="left:767px;top:489px"></span><span class="field" style="left:785px;top:488px">PCM/ICD</span>

  <span class="box" style="left:64px;top:529px"></span><span class="field" style="left:87px;top:528px">Diabetes</span>
  <span class="box" style="left:236px;top:529px"></span><span class="field" style="left:259px;top:528px">Claustrophopbia</span>
  <span class="box" style="left:414px;top:529px"></span><span class="field" style="left:437px;top:528px">Asthma</span>
  <span class="box" style="left:580px;top:529px"></span><span class="field" style="left:603px;top:528px">Emphysema</span>
  <span class="box" style="left:767px;top:529px"></span><span class="field" style="left:790px;top:528px">COPD</span>

  <span class="field" style="left:64px;top:566px">LMP:</span><div class="line" style="left:93px;top:578px;width:102px"></div>
  <span class="box" style="left:236px;top:568px"></span><span class="field" style="left:259px;top:567px">bHCG</span>
  <span class="box" style="left:414px;top:568px"></span><span class="field" style="left:437px;top:567px">Tubal ligation</span>
  <span class="box" style="left:580px;top:568px"></span><span class="field" style="left:603px;top:567px">Post-menopause &gt; 1 year</span>
  <span class="box" style="left:767px;top:568px"></span><span class="field" style="left:790px;top:566px">Hysterectomy</span>

  <div class="abs alert">PLEASE READ THE FOLLOWING INSTRUCTIONS CAREFULLY. YOU MIGHT BE RESCHEDULED IF ANY OF THE FOLLOWING INSTRUCTIONS ARE NOT MET.</div>

  <ul class="steps">
    <li style="top:0;white-space:normal">AVOID <b>caffeine</b> containing products (coffee, tea, soda, chocolate, energy drinks, or some over the counter medications) for 4 hours prior to testing.</li>
    <li style="top:44px">AVOID <b>smoking</b> for 4 hours prior to testing.</li>
    <li style="top:72px">AVOID <b>eating</b> or <b>drinking</b> anything except water for 4 hours prior to testing.</li>
    <li style="top:100px">Arrive 15 minutes early for your appointment time.</li>
    <li style="top:128px;white-space:normal">Wear comfortable clothing. <i>Remove any metal objects</i>, such as jewelry or piercings. Women will be asked to remove bras containing metal underwire.</li>
    <li style="top:171px">Inform your physician or the staff if you are <i>claustrophobic</i> or have a problem staying in restricted environments for any length of time.</li>
    <li style="top:199px">Inform the physician or the staff if you are or think you might be <i>pregnant</i>.</li>
  </ul>

  <p class="abs ack">I hereby acknowledge that the instructions and procedures pertinent to this study were explained thoroughly, I had time to ask questions, and these questions were addressed satisfactorily.</p>

  <div class="line" style="left:64px;top:1020px;width:213px"></div>
  <div class="line" style="left:313px;top:1020px;width:213px"></div>
  <span class="sig-label" style="left:64px;top:1026px">Patient’s print name</span>
  <span class="sig-label" style="left:313px;top:1026px">Patient’s signature</span>
  <div class="line" style="left:64px;top:1082px;width:213px"></div>
  <div class="line" style="left:313px;top:1082px;width:213px"></div>
  <span class="sig-label" style="left:64px;top:1088px">Prescriber’s print name</span>
  <span class="sig-label" style="left:313px;top:1088px">Prescriber’s signature</span>

  <div class="band" style="left:562px;top:1003px;width:294px;height:24px;font-size:14px">REFERRING PHYSICIAN CONTACT INFORMATION</div>
  <div class="sched-row" style="left:562px;width:294px;top:1028px">Order date:</div>
  <div class="sched-row" style="left:562px;width:294px;top:1052px">Tel no.:</div>
  <div class="sched-row" style="left:562px;width:294px;top:1076px">Fax no.:</div>

  <div class="abs footer">Crestline Cardio, PLLC.<br>Visit us at 218 Juniper Ave., Ste. B, Webster, TX 77412. For appointments or more information on testing, please call <b>(713) 642 1187,</b> or visit <b>www.crestlinecardio.example</b>.</div>
</main>
</body>
</html>
```